Brand new letterhead, business card, email signature etc.

We are a financial company in London, UK. Our website is www.quorvane.com. We're wanting a complete remodel of the company colours, letter head, business cards, email signatures, etc. Looking to keep the same font for the company name. I have upload a colour palette that we want to work with. We're looking for company letterhead for outgoing letters/ correspondence, letterhead for internal documentation, email signatures, e-letters. etc. Ultimately we will redesign the entire website also. It is important that our clients get a strong, secure, warm, trustworthy, solid feeling and first impression.
Updates

Designs look the same

Target Market(s)

Institutional investors, (ultra) high net worth individuals

Industry/Entity Type

Finance, Invesments banking.

Font styles to use
Other font styles liked:
• Current font is "Champagne & Limousines"

Requirements
Must have
• Must use the colours provided on the PDF uploaded to the portal. The purple = main colour. The red = accent colour.
Nice to have
• Nice to use same font as now for the company name "Marlowin". Font is "Champagne & Limousines". Nice to have some reference to the old logo flower, but only subtle.
Should not have
• Do not use the colour red from our website. Use the colours provided on the colour palette PDF that I uploaded in the portal.

```html
<!DOCTYPE html>
<html lang="en">
<head>
<meta charset="utf-8">
<title>Marlowin Stationery</title>
<link rel="stylesheet" href="https://fonts.googleapis.com/css2?family=Montserrat:wght@300;400;500;700&display=swap">
<style>
  :root {
    --brand-purple: #4b2d63;
    --accent-red: #c1202f;
    --ink: #1c1c1c;
    --paper: #ffffff;
    --backdrop: #eeeeef;
  }
  * { margin: 0; padding: 0; box-sizing: border-box; }
  html, body { width: 1200px; height: 1200px; overflow: hidden; }
  body {
    background: var(--backdrop);
    font-family: "Montserrat", Arial, sans-serif;
    color: var(--ink);
    position: relative;
  }
  .piece {
    position: absolute; background: var(--paper); overflow: hidden;
    box-shadow: 0 12px 26px rgba(0, 0, 0, 0.22);
  }

  /* brand lockup */
  .lockup { display: flex; align-items: center; position: absolute; }
  .lockup-square { border: 1.5px solid var(--accent-red); flex: none; }
  .lockup-name { font-weight: 300; letter-spacing: 0.08em; line-height: 1; text-transform: uppercase; color: var(--brand-purple); }

  /* faint floral decoration placeholder */
  .decor-area { position: absolute; border-radius: 50%; }

  .icon { width: 12px; height: 12px; flex: none; }
  ul { list-style: none; }

  /* letterhead */
  .letterhead { left: 226px; top: 72px; width: 746px; height: 1056px; }
  .letterhead .lockup { left: 209px; top: 58px; gap: 20px; }
  .letterhead .lockup-square { width: 80px; height: 80px; }
  .letterhead .lockup-name { font-size: 40px; }
  .letterhead .decor-area {
    left: 20px; top: 270px; width: 520px; height: 720px;
    background: radial-gradient(ellipse at center, rgba(75,45,99,0.05), rgba(75,45,99,0) 70%);
  }
  .letterhead-contacts {
    position: absolute; left: 36px; top: 954px;
    font-size: 16px; line-height: 22px;
  }
  .letterhead-contacts li, .letterhead-address li { display: flex; align-items: center; gap: 12px; }
  .letterhead-contacts .icon { color: var(--brand-purple); }
  .letterhead-address {
    position: absolute; right: 32px; top: 954px;
    font-size: 16px; line-height: 18.5px; text-align: right;
  }
  .letterhead-address li { justify-content: flex-end; }
  .letterhead-address .icon { color: var(--brand-purple); }
  .letterhead-band { position: absolute; left: 0; top: 1014px; }

  /* business card front */
  .card-front { left: 709px; top: 281px; width: 436px; height: 257px; }
  .card-front .lockup { left: 35px; top: 29px; gap: 14px; }
  .card-front .lockup-square { width: 60px; height: 60px; }
  .card-front .lockup-name { font-size: 30px; }
  .card-person { position: absolute; left: 35px; top: 168px; }
  .person-name { font-weight: 700; font-size: 15px; letter-spacing: 0.04em; text-transform: uppercase; }
  .card-person .person-name { color: var(--brand-purple); }
  .person-role { font-size: 11px; margin-top: 4px; }
  .card-divider { position: absolute; left: 238px; top: 108px; width: 8px; height: 149px; background: var(--accent-red); }
  .card-panel {
    position: absolute; left: 246px; top: 108px; width: 190px; height: 149px;
    background: var(--brand-purple); color: var(--paper);
    padding: 24px 22px 0 0; font-size: 11px; line-height: 15px; text-align: right;
  }
  .card-panel li { display: flex; justify-content: flex-end; gap: 10px; align-items: flex-start; }
  .card-panel .icon { width: 10px; height: 10px; margin-top: 2px; }
  .card-panel .gap { margin-top: 9px; }

  /* business card back */
  .card-back { left: 709px; top: 679px; width: 436px; height: 256px; background: var(--brand-purple); }
  .card-back .decor-area {
    left: 200px; top: -40px; width: 280px; height: 320px;
    background: radial-gradient(ellipse at center, rgba(255,255,255,0.09), rgba(255,255,255,0) 70%);
  }
  .card-back .lockup { left: 62px; top: 90px; gap: 18px; }
  .card-back .lockup-square { width: 76px; height: 76px; border-color: var(--paper); }
  .card-back .lockup-name { font-size: 35px; color: var(--paper); }

  /* email signature */
  .email-signature { left: 72px; top: 797px; width: 599px; height: 138px; }
  .email-signature .decor-area {
    left: 90px; top: -10px; width: 160px; height: 160px;
    background: radial-gradient(ellipse at center, rgba(75,45,99,0.05), rgba(75,45,99,0) 70%);
  }
  .email-signature .lockup { left: 34px; top: 44px; gap: 10px; }
  .email-signature .lockup-square { width: 49px; height: 49px; }
  .email-signature .lockup-name { font-size: 22px; }
  .signature-shape { position: absolute; left: 0; top: 0; }
  .signature-person { position: absolute; right: 40px; top: 20px; text-align: right; color: var(--paper); }
  .signature-person .person-name { font-size: 13px; }
  .signature-person .person-role { font-size: 11px; margin-top: 2px; }
  .signature-contacts {
    position: absolute; right: 158px; top: 70px; color: var(--paper);
    font-size: 11px; line-height: 18px; text-align: right;
  }
  .signature-address {
    position: absolute; right: 40px; top: 70px; color: var(--paper);
    font-size: 11px; line-height: 15px; text-align: right;
  }
  .signature-contacts li, .signature-address li { display: flex; justify-content: flex-end; gap: 8px; align-items: center; }
  .signature-contacts .icon, .signature-address .icon { width: 10px; height: 10px; }
</style>
</head>
<body>

<svg width="0" height="0" style="position:absolute">
  <defs>
    <symbol id="icon-mail" viewBox="0 0 12 12"><rect x="0.8" y="2.5" width="10.4" height="7" fill="none" stroke="currentColor" stroke-width="1.2"/><path d="M0.8 2.8 L6 6.8 L11.2 2.8" fill="none" stroke="currentColor" stroke-width="1.1"/></symbol>
    <symbol id="icon-globe" viewBox="0 0 12 12"><circle cx="6" cy="6" r="5" fill="none" stroke="currentColor" stroke-width="1.1"/><path d="M1 6 H11 M6 1 C3.5 3.5 3.5 8.5 6 11 M6 1 C8.5 3.5 8.5 8.5 6 11" fill="none" stroke="currentColor" stroke-width="0.8"/></symbol>
    <symbol id="icon-pin" viewBox="0 0 12 12"><path d="M6 0.8 C3.8 0.8 2.4 2.4 2.4 4.3 C2.4 6.8 6 10 6 10 C6 10 9.6 6.8 9.6 4.3 C9.6 2.4 8.2 0.8 6 0.8 Z" fill="none" stroke="currentColor" stroke-width="1.4"/><circle cx="6" cy="4.4" r="1.3" fill="currentColor"/><rect x="2" y="10.6" width="8" height="1.2" fill="currentColor"/></symbol>
  </defs>
</svg>

<!-- Letterhead -->
<section class="piece letterhead" aria-label="Letterhead">
  <div class="decor-area" role="img" aria-label="Faint line-drawn flower decoration"></div>
  <div class="lockup"><span class="lockup-square"></span><span class="lockup-name">Marlowin</span></div>
  <ul class="letterhead-contacts">
    <li><svg class="icon"><use href="#icon-mail"/></svg>info@quorvane.com</li>
    <li><svg class="icon"><use href="#icon-globe"/></svg>www.quorvane.com</li>
  </ul>
  <ul class="letterhead-address">
    <li>14th Floor <svg class="icon"><use href="#icon-pin"/></svg></li>
    <li style="padding-right:24px">52 Aldgate Row</li>
    <li style="padding-right:24px">London</li>
    <li style="padding-right:24px">EC3N 2LT</li>
  </ul>
  <svg class="letterhead-band" width="746" height="16" viewBox="0 0 746 16">
    <path d="M0 1 H430 C438 1 442 14 452 14 H0 Z" fill="var(--brand-purple)"/>
  </svg>
</section>

<!-- Business card front -->
<section class="piece card-front" aria-label="Business card front">
  <div class="lockup"><span class="lockup-square"></span><span class="lockup-name">Marlowin</span></div>
  <div class="card-person">
    <p class="person-name">Dorian Pellow</p>
    <p class="person-role">Executive Director</p>
  </div>
  <div class="card-divider"></div>
  <ul class="card-panel">
    <li>info@quorvane.com <svg class="icon"><use href="#icon-mail"/></svg></li>
    <li>www.quorvane.com <svg class="icon"><use href="#icon-globe"/></svg></li>
    <li class="gap">14th Floor <svg class="icon"><use href="#icon-pin"/></svg></li>
    <li style="padding-right:20px">52 Aldgate Row</li>
    <li style="padding-right:20px">London</li>
    <li style="padding-right:20px">EC3N 2LT</li>
  </ul>
</section>

<!-- Business card back -->
<section class="piece card-back" aria-label="Business card back">
  <div class="decor-area" role="img" aria-label="Faint line-drawn flower decoration"></div>
  <div class="lockup"><span class="lockup-square"></span><span class="lockup-name">Marlowin</span></div>
</section>

<!-- Email signature -->
<section class="piece email-signature" aria-label="Email signature">
  <div class="decor-area" role="img" aria-label="Faint line-drawn flower decoration"></div>
  <div class="lockup"><span class="lockup-square"></span><span class="lockup-name">Marlowin</span></div>
  <svg class="signature-shape" width="599" height="138" viewBox="0 0 599 138">
    <polygon points="266,0 284,0 318,138 300,138" fill="var(--accent-red)"/>
    <polygon points="284,0 599,0 599,138 318,138" fill="var(--brand-purple)"/>
  </svg>
  <div class="signature-person">
    <p class="person-name">Dorian Pellow</p>
    <p class="person-role">Executive Director</p>
  </div>
  <ul class="signature-contacts">
    <li>info@quorvane.com <svg class="icon"><use href="#icon-mail"/></svg></li>
    <li>www.quorvane.com <svg class="icon"><use href="#icon-globe"/></svg></li>
  </ul>
  <ul class="signature-address">
    <li>14th Floor <svg class="icon"><use href="#icon-pin"/></svg></li>
    <li style="padding-right:18px">52 Aldgate Row</li>
    <li style="padding-right:18px">London</li>
    <li style="padding-right:18px">EC3N 2LT</li>
  </ul>
</section>

</body>
</html>
```